Coastal Bright Sweep Business Card

We are a cleaning and waste management company with the slogan "making waste to landfill a thing of the past". We would like a re-design of our current business card. On the front we want to continue to use our logo as the focus point. On the back, we want the whole thing re-done to be less busy. We want the staff member’s name, the job title, mobile number, email and website. We do not want the address on the card. We still want the green, black and blue colours used, but a new font for the information on the back. Please do not change the logo design at all. We are also thinking about using icons to replace the text ‘mobile, email, website’. The “events + commercial” banner needs to be incorporated somewhere and needs to read “events + commercial + waste”. Another important point for consideration is that we are very concerned about being environmentally sustainable and will be printing on recycled paper. All designs should be made to compliment this in regards to boldness and colouring. Please find attached our logo, our colour chart and an image of our current business card.

```html
<!DOCTYPE html>
<html lang="en">
<head>
<meta charset="utf-8">
<title>Coastal Bright Sweep Business Card</title>
<link rel="stylesheet" href="https://fonts.googleapis.com/css2?family=Arvo:wght@400;700&family=Raleway:wght@400;500&display=swap">
<style>
  :root {
    --backdrop: #2a2a2c;
    --navy: #1d4680;
    --navy-deep: #173a6d;
    --sky: #2ba7e0;
    --leaf: #7cc242;
    --paper: #ffffff;
    --ink-light: #ffffff;
  }
  html, body {
    margin: 0;
    width: 1200px;
    height: 873px;
    overflow: hidden;
    background: var(--backdrop);
  }
  .canvas {
    position: relative;
    width: 1200px;
    height: 873px;
  }
  .card {
    position: absolute;
    width: 520px;
    height: 300px;
    overflow: hidden;
    box-shadow: 0 14px 30px rgba(0,0,0,0.45);
  }
  .card svg.card-art {
    position: absolute;
    inset: 0;
    width: 100%;
    height: 100%;
  }
  .card-front { left: 70px; top: 130px; }
  .card-back { left: 610px; top: 440px; background: var(--paper); }

  .front-name {
    position: absolute;
    left: 0; right: 0; top: 92px;
    text-align: center;
    font-family: "Arvo", serif;
    font-weight: 700;
    font-size: 36px;
    line-height: 1.05;
    color: var(--ink-light);
  }

  .back-name {
    position: absolute;
    left: 28px; top: 104px;
    font-family: "Arvo", serif;
    font-weight: 700;
    font-size: 28px;
    line-height: 1.02;
    color: var(--navy);
    display: flex;
    align-items: center;
    gap: 10px;
  }
  .back-name .mark-dot {
    width: 14px; height: 14px;
    border-radius: 50%;
    background: var(--leaf);
    flex: none;
  }
  .staff {
    position: absolute;
    right: 26px; top: 26px;
    text-align: right;
    font-family: "Arvo", serif;
  }
  .staff-name {
    font-weight: 700;
    font-size: 17px;
    letter-spacing: 1px;
    color: var(--navy);
  }
  .staff-role {
    font-size: 12px;
    letter-spacing: 1.5px;
    color: var(--leaf);
  }
  .contact {
    position: absolute;
    right: 22px; top: 150px;
    margin: 0; padding: 0;
    list-style: none;
    font-family: "Raleway", sans-serif;
    font-size: 11.5px;
    color: var(--ink-light);
  }
  .contact li {
    display: flex;
    justify-content: flex-end;
    align-items: center;
    gap: 8px;
    height: 22px;
    white-space: nowrap;
  }
  .contact svg { width: 14px; height: 14px; flex: none; }
  .divider {
    position: absolute;
    left: 150px; right: 20px; top: 230px;
    border-top: 1px solid rgba(255,255,255,0.7);
  }
  .services {
    position: absolute;
    left: 0; right: 0; bottom: 14px;
    text-align: center;
    font-family: "Arvo", serif;
    font-size: 15px;
    letter-spacing: 7px;
    color: var(--ink-light);
  }
</style>
</head>
<body>
<main class="canvas">

  <section class="card card-front" aria-label="Card front">
    <svg class="card-art" viewBox="0 0 520 300" preserveAspectRatio="none" aria-hidden="true">
      <defs>
        <linearGradient id="frontBlue" x1="0" y1="0" x2="1" y2="1">
          <stop offset="0" stop-color="#1d4c8a"/>
          <stop offset="1" stop-color="#173a6d"/>
        </linearGradient>
      </defs>
      <rect width="520" height="300" fill="url(#frontBlue)"/>
      <path d="M0 300 C170 250 380 250 520 110 L520 300 Z" fill="var(--leaf)"/>
      <path d="M0 300 C180 262 390 262 520 124 L520 300 Z" fill="var(--sky)"/>
      <path d="M0 300 C200 280 400 290 520 200 L520 300 Z" fill="var(--sky)" opacity="0.7"/>
    </svg>
    <div class="front-name">Coastal<br>Bright Sweep</div>
  </section>

  <section class="card card-back" aria-label="Card back">
    <svg class="card-art" viewBox="0 0 520 300" preserveAspectRatio="none" aria-hidden="true">
      <path d="M0 212 C120 266 260 116 520 66" fill="none" stroke="var(--leaf)" stroke-width="7"/>
      <path d="M0 224 C120 278 260 128 520 78" fill="none" stroke="var(--sky)" stroke-width="7"/>
      <path d="M0 236 C120 290 260 140 520 90 L520 300 L0 300 Z" fill="var(--navy)"/>
    </svg>

    <div class="staff">
      <div class="staff-name">MORGAN ELLERY</div>
      <div class="staff-role">CLIENT MANAGER</div>
    </div>

    <div class="back-name"><span class="mark-dot"></span><span>Coastal<br>Bright Sweep</span></div>

    <ul class="contact">
      <li>0400 555 218
        <svg viewBox="0 0 14 14"><rect x="3.5" y="0.5" width="7" height="13" rx="1.5" fill="none" stroke="var(--leaf)" stroke-width="1.2"/><circle cx="7" cy="11.2" r="0.9" fill="var(--leaf)"/></svg>
      </li>
      <li>mellery@coastalbrightsweep.com.au
        <svg viewBox="0 0 14 14"><rect x="0.5" y="2.5" width="13" height="9" fill="var(--leaf)"/><path d="M0.5 2.5 L7 8 L13.5 2.5" fill="none" stroke="var(--navy)" stroke-width="1"/></svg>
      </li>
      <li>www.coastalbrightsweep.com.au
        <svg viewBox="0 0 14 14"><circle cx="7" cy="7" r="6" fill="none" stroke="var(--leaf)" stroke-width="1.2"/><ellipse cx="7" cy="7" rx="2.6" ry="6" fill="none" stroke="var(--leaf)" stroke-width="1"/><path d="M1 7 H13" stroke="var(--leaf)" stroke-width="1"/></svg>
      </li>
    </ul>

    <div class="divider"></div>
    <div class="services">EVENTS + COMMERCIAL + WASTE</div>
  </section>

</main>
</body>
</html>
```